Bluefinch Painting needs a Website

We need a website built for a Painting company I own, we mainly do residential painting, but don't want to be limited to that.

Need to have estimate request form.
Need pic's of past projects

I like the look of the website for http://www.harborline-painters.example
& "Wexley Property inspections"

My logo that was designed here on ArtHive on the front page

I would like one of the houses I downloaded as part of the background
of the front page.

Target Market(s)

Home owners

Industry/Entity Type

Painting

Number of Pages Required

1 page

Font styles to use
Serif

Requirements
Must have
• Estimate request form for home owners to fill out -
• Name:
• Phone Number:
• Address:
• E-mail:
• Painting project description:
• And my info to:
• My phone number: (555) 318-7046
• My web address bluefinchpainting.example
Nice to have
• My logo that was designed here on ArtHive

```html
<!DOCTYPE html>
<html lang="en">
<head>
<meta charset="utf-8">
<title>Bluefinch Painting</title>
<link rel="stylesheet" href="https://fonts.googleapis.com/css2?family=Raleway:wght@300;400;500;600;700&family=Tinos&display=swap">
<style>
:root{
  --brand:#1f4fa0;
  --brand-light:#3a8fd8;
  --welcome:#1b6db0;
  --field:#efefef;
  --field-text:#a9a9a9;
  --ink:#3c3c3c;
  --footer:#222222;
  --white:#ffffff;
}
*{margin:0;padding:0;box-sizing:border-box}
html,body{width:1200px;height:2599px;overflow:hidden;background:var(--white)}
body{position:relative;font-family:"Raleway",sans-serif;color:var(--ink)}
.abs{position:absolute}

/* Hero */
.hero{left:0;top:0;width:1200px;height:528px;
  background:linear-gradient(180deg,#2b4a78 0%,#5f7fa8 28%,#4a5560 55%,#3d4a3a 78%,#5a7a3e 100%)}
.hero-shade{left:0;top:0;width:1200px;height:528px;background:linear-gradient(90deg,rgba(0,0,0,.05),rgba(0,0,0,.25))}
.brand{display:flex;align-items:center;gap:10px;color:var(--white);font-weight:600;font-size:26px;letter-spacing:2px;text-transform:uppercase}
.brand-mark{width:28px;height:28px;background:var(--white);border-radius:50%}
.hero .brand{left:88px;top:40px}
.nav{left:470px;top:52px;display:flex;align-items:center;font-size:13px;letter-spacing:1px;color:var(--white)}
.nav a{color:var(--white);text-decoration:none;margin-right:56px}
.nav .quote-btn{margin-right:0;border:2px solid var(--white);border-radius:3px;padding:5px 22px;font-weight:700;font-size:11px}
.hero-phone{left:962px;top:45px;font-size:24px;color:var(--white)}
.slider-dots{left:86px;top:284px;display:flex;flex-direction:column;gap:8px}
.slider-dots span{width:9px;height:9px;border-radius:50%;border:1px solid var(--white)}
.slider-dots span:first-child{background:var(--white)}
.hero-title{right:85px;top:236px;font-size:28px;font-weight:700;color:var(--white);letter-spacing:1px;text-align:right;text-shadow:0 1px 3px rgba(0,0,0,.5)}
.hero-sub{right:85px;top:272px;font-size:17px;font-weight:600;color:var(--white);text-shadow:0 1px 3px rgba(0,0,0,.5)}
.btn{display:flex;align-items:center;justify-content:center;background:var(--brand);color:var(--white);font-size:11px;font-weight:700;letter-spacing:.5px;border-radius:2px}
.hero .btn{left:912px;top:330px;width:201px;height:36px}
.hero-own{right:85px;top:384px;font-size:12px;color:var(--white)}
.hero-own b{font-weight:700}

/* Estimate form */
.form-title{left:104px;top:574px;font-size:37px;font-weight:400;color:#444}
.form-btn{left:888px;top:572px;width:202px;height:36px}
.field{background:var(--field);color:var(--field-text);font-size:11px;letter-spacing:.5px;padding:14px 26px;border-bottom:4px solid var(--white)}
.f1{left:104px;top:634px;width:429px;height:48px}
.f2{left:104px;top:682px;width:429px;height:48px}
.f3{left:104px;top:730px;width:429px;height:48px}
.f4{left:104px;top:778px;width:429px;height:46px}
.f5{left:538px;top:634px;width:552px;height:190px;border-bottom:0}

/* Welcome */
.welcome{left:0;top:895px;width:1200px;height:420px;background:var(--welcome);color:var(--white)}
.welcome h2{position:absolute;left:110px;top:54px;font-size:30px;font-weight:400;letter-spacing:.5px}
.welcome .rule{position:absolute;left:110px;top:98px;width:718px;height:1px;background:rgba(255,255,255,.45)}
.welcome .lead{position:absolute;left:110px;top:124px;font-size:13px;font-weight:700}
.welcome p.body{position:absolute;left:110px;width:720px;font-size:12.5px;line-height:16px}
.welcome .b1{top:152px}
.welcome .b2{top:262px}
.paint-can{left:878px;top:0;width:220px;height:385px;border-radius:0 0 14px 14px;background:linear-gradient(180deg,#2a5fa0 0%,#1d3f7a 60%,#16336a 100%);box-shadow:0 6px 14px rgba(0,0,0,.3)}

/* Gallery */
.photo{overflow:hidden}
.g1{left:106px;top:1386px;width:719px;height:241px;background:linear-gradient(180deg,#9fb4c8,#8a8f95 50%,#6a6f6c)}
.g2{left:825px;top:1386px;width:269px;height:459px;background:linear-gradient(180deg,#b9c7d3,#7e7a70 45%,#6d6860 80%,#8b8378)}
.g3{left:106px;top:1627px;width:335px;height:218px;background:linear-gradient(180deg,#b8d0e8,#8d9070 55%,#a6a6a0)}
.g4{left:441px;top:1627px;width:384px;height:218px;background:linear-gradient(180deg,#3b7fc0,#1f5a94)}
.g5{left:106px;top:1845px;width:270px;height:455px;background:linear-gradient(180deg,#b5cde6,#9a9178 45%,#6f7a4e 75%,#8f8a80)}
.g6{left:376px;top:1845px;width:718px;height:238px;background:linear-gradient(180deg,#c4d5e6,#4a4d4e 45%,#3d4a36 80%,#6c6f6a)}
.g7{left:376px;top:2083px;width:382px;height:217px;background:linear-gradient(180deg,#b7d0ea,#8a8a7a 45%,#b4b4b0)}
.g8{left:758px;top:2083px;width:336px;height:217px;background:linear-gradient(180deg,#c6d8ea,#8e8a7c 45%,#5e7a44)}
.hover-label{position:absolute;left:0;top:0;width:100%;height:100%;display:flex;flex-direction:column;align-items:center;justify-content:center;gap:10px;color:var(--white);font-size:13px;font-weight:600;letter-spacing:.5px;text-align:center;line-height:18px}

/* Footer */
.footer{left:0;top:2373px;width:1200px;height:226px;background:var(--footer);color:var(--white)}
.footer-nav{position:absolute;left:88px;top:50px;list-style:none;font-size:12px;line-height:24px;letter-spacing:.5px}
.footer-nav li:first-child{color:var(--brand-light)}
.footer-call{position:absolute;left:428px;top:50px;width:260px}
.footer-call h3{font-size:14px;font-weight:700;letter-spacing:.5px}
.footer-call .phone{font-size:28px;color:var(--brand-light);margin-top:6px}
.footer-call .web{font-size:17px;margin-top:4px;letter-spacing:.5px}
.footer .brand{position:absolute;left:770px;top:52px;color:var(--brand-light)}
.footer .brand-mark{background:var(--brand-light)}
.copyright{position:absolute;left:815px;top:117px;font-family:"Tinos",serif;font-size:13px;color:#cfcfcf}
.social{position:absolute;left:983px;top:146px;display:flex;gap:12px}
.social span{width:18px;height:18px;background:#555;border-radius:2px}
.social span:first-child{background:var(--brand-light)}
</style>
</head>
<body>

<header class="abs hero" role="img" aria-label="Photo of a freshly painted two-storey family house with garage and front garden">
</header>
<div class="abs hero-shade"></div>
<div class="abs brand"  style="left:88px;top:40px"><span class="brand-mark"></span>Bluefinch Painting</div>
<nav class="abs nav">
  <a href="#about">ABOUT</a>
  <a href="#services">SERVICES</a>
  <a href="#projects">PROJECTS</a>
  <a href="#quote" class="quote-btn">FREE QUOTE</a>
</nav>
<div class="abs hero-phone">(555) 318-7046</div>
<div class="abs slider-dots"><span></span><span></span><span></span></div>
<h1 class="abs hero-title">EXTERIOR - INTERIOR&nbsp; RESIDENTIAL - COMMERCIAL</h1>
<div class="abs hero-sub">We offer Interior and Exterior House Painting throughout the USA</div>
<a class="abs btn" style="left:912px;top:330px;width:201px;height:36px;text-decoration:none">GET QUOTE FOR FREE</a>
<div class="abs hero-own">Own a House? <b>GET YOUR FREE QUOTE NOW!</b></div>

<section id="quote">
  <h2 class="abs form-title">Estimate Request Form</h2>
  <div class="abs btn form-btn">GET QUOTE NOW!</div>
  <div class="abs field f1">NAME*</div>
  <div class="abs field f2">PHONE NUMBER*</div>
  <div class="abs field f3">ADDRESS*</div>
  <div class="abs field f4">E-MAIL*</div>
  <div class="abs field f5">PAINTING PROJECT DESCRIPTION ...</div>
</section>

<section class="abs welcome" id="about">
  <h2>WELCOME TO BLUEFINCH PAINTING</h2>
  <div class="rule"></div>
  <p class="lead">We offer Interior and Exterior House Painting throughout the USA.</p>
  <p class="body b1">Lorem ipsum dolor sit amet, consectetuer adipiscing elit, sed diam nonummy nibh euismod tincidunt ut laoreet dolore magna aliquam erat volutpat. Ut wisi enim ad minim veniam, quis nostrud exerci tation ullamcorper suscipit lobortis nisl ut aliquip ex ea commodo consequat. Duis autem vel eum iriure dolor in hendrerit in vulputate velit esse molestie consequat, vel illum dolore eu feugiat nulla facilisis at vero eros et accumsan et iusto odio dignissim qui blandit praesent luptatum zzril delenit augue duis dolore te feugait nulla facilisi.</p>
  <p class="body b2">Duis autem vel eum iriure dolor in hendrerit in vulputate velit esse molestie consequat, vel illum dolore eu feugiat nulla facilisis at vero eros et accumsan et iusto odio dignissim qui blandit praesent luptatum zzril delenit augue duis dolore te feugait nulla facilisi.Lorem ipsum dolor sit amet, consectetuer adipiscing elit, sed diam nonummy nibh euismod tincidunt ut laoreet dolore magna aliquam erat volutpat. Ut wisi enim ad minim veniam, quis nostrud exerci tation ullamcorper suscipit lobortis nisl ut aliquip ex ea commodo consequat.</p>
  <div class="abs paint-can" role="img" aria-label="Illustration of a blue paint can with a roller and a 'We carry Hollis Paints' badge"></div>
</section>

<section id="projects">
  <div class="abs photo g1" role="img" aria-label="Photo of a large grey two-storey house with tall windows"></div>
  <div class="abs photo g2" role="img" aria-label="Photo of a beige house entrance with stone path and pink flowers"></div>
  <div class="abs photo g3" role="img" aria-label="Photo of company work vans and a pickup truck in front of a house"></div>
  <div class="abs photo g4" role="img" aria-label="Photo of a painted house under a blue hover overlay">
    <div class="hover-label">
      <svg width="26" height="26" viewBox="0 0 26 26" aria-hidden="true"><circle cx="13" cy="13" r="11.5" fill="none" stroke="#fff" stroke-width="2"/><path d="M13 7v12M7 13h12" stroke="#fff" stroke-width="2"/></svg>
      <span>EXTERIOR HOUSE<br>PAINTING</span>
    </div>
  </div>
  <div class="abs photo g5" role="img" aria-label="Photo of a craftsman house with garden path and flowers"></div>
  <div class="abs photo g6" role="img" aria-label="Photo of a dark painted house with garage and trees"></div>
  <div class="abs photo g7" role="img" aria-label="Photo of a pickup truck and work van parked by a house"></div>
  <div class="abs photo g8" role="img" aria-label="Photo of a beige house with flowering shrubs"></div>
</section>

<footer class="abs footer">
  <ul class="footer-nav">
    <li>HOME</li><li>ABOUT</li><li>SERVICES</li><li>PROJECTS</li><li>FREE QUOTE</li>
  </ul>
  <div class="footer-call">
    <h3>CALL FOR A FREE QUOTE</h3>
    <div class="phone">(555) 318-7046</div>
    <div class="web">bluefinchpainting.example</div>
  </div>
  <div class="brand"><span class="brand-mark"></span>Bluefinch Painting</div>
  <div class="copyright">© 2014 Bluefinch Painting. All Rights Reserved.</div>
  <div class="social"><span></span><span></span><span></span><span></span></div>
</footer>

</body>
</html>
```